Tesmaro Realty Business Cards

Design business card

Target Market(s)

High-End Buyer of Real Estate over $1 million dollars

Industry/Entity Type

Realtor

Contact Information for Business Card

Lina Tesmaro R(S) LIC.# 41927
Cell 808 555-0163
Email Lina@Tesmaro.net
Website PeakHomeFinds.com

Also Need Cards for:

Glen Tesmaro R(B) LIC# 60418
C 808 555-0192
E Glen@Tesmaro.net
W PeakHomeFinds.com

Colors

Designer to choose colors to be used in the design.

Requirements
Must have
• Address on back:
• 57 Oleander Ct. , Wailea HI 96721
• Logo on back
Nice to have
• I would like the phone numbers and email address to be big so people can read it easily
Should not have
• Very small print Except For: address (57 Oleander Ct. Wailea HI 96721)

```html
<!DOCTYPE html>
<html lang="en">
<head>
<meta charset="utf-8">
<title>Tesmaro Realty Business Cards</title>
<link href="https://fonts.googleapis.com/css2?family=Cinzel:wght@500;700&display=swap" rel="stylesheet">
<style>
  :root {
    --stage: #e9e9e9;
    --card-grey: #9a9a9a;
    --card-white: #ffffff;
    --ink-light: #ffffff;
    --ink-dark: #111111;
    --photo-warm: #d9b9a6;
    --photo-cool: #3a3d48;
  }
  * { margin: 0; padding: 0; box-sizing: border-box; }
  html, body { width: 1200px; height: 1000px; overflow: hidden; }
  body {
    background: var(--stage);
    font-family: "Cinzel", serif;
    position: relative;
  }
  .card {
    position: absolute;
    top: 185px;
    width: 360px;
    height: 630px;
    overflow: hidden;
    box-shadow: 0 10px 30px rgba(0,0,0,0.18);
  }
  .card--front { left: 180px; background: var(--card-white); }
  .card--back { left: 660px; background: var(--card-grey); }

  .front-photo {
    position: absolute;
    left: 150px;
    top: 130px;
    width: 210px;
    height: 140px;
    background: linear-gradient(90deg, var(--photo-warm) 0%, #e7cfc2 45%, var(--photo-cool) 100%);
  }
  .front-band {
    position: absolute;
    left: 0; right: 0; top: 270px; bottom: 0;
    background: linear-gradient(180deg, #a3a3a3 0%, var(--card-grey) 100%);
    padding: 48px 24px 0;
    text-align: center;
    color: var(--ink-light);
  }
  .agent-name {
    font-size: 17px;
    font-weight: 500;
    letter-spacing: 0.04em;
    margin-bottom: 26px;
  }
  .agent-phone {
    font-size: 19px;
    font-weight: 700;
    color: var(--ink-dark);
    letter-spacing: 0.06em;
    margin-bottom: 12px;
  }
  .agent-email, .agent-web {
    font-size: 17px;
    font-weight: 500;
    letter-spacing: 0.05em;
    margin-bottom: 10px;
  }

  .back-brand {
    position: absolute;
    left: 0; right: 0; top: 50%;
    transform: translateY(-50%);
    text-align: center;
    color: var(--ink-light);
    font-size: 40px;
    font-weight: 700;
    letter-spacing: 0.12em;
    line-height: 1.35;
  }
  .back-address {
    position: absolute;
    left: 0; right: 0; bottom: 44px;
    text-align: center;
    color: var(--ink-light);
    font-size: 13px;
    font-weight: 500;
    letter-spacing: 0.05em;
  }
</style>
</head>
<body>
  <section class="card card--front" aria-label="Business card front">
    <div class="front-photo" role="img" aria-label="Portrait photograph of the two agents"></div>
    <div class="front-band">
      <p class="agent-name">Lina Tesmaro R(S) LIC.# 41927</p>
      <p class="agent-phone">808 555-0163</p>
      <p class="agent-email">Lina@Tesmaro.net</p>
      <p class="agent-web">www.PeakHomeFinds.com</p>
    </div>
  </section>

  <section class="card card--back" aria-label="Business card back">
    <p class="back-brand">Tesmaro<br>Realty</p>
    <p class="back-address">57 Oleander Ct., Wailea HI 96721</p>
  </section>
</body>
</html>
```